Im open to ideas.. I was thinking on my business cards aswell as my logo. a place for my name. email. phone number and abn..

ive attched a file with my business logo. which i dont love the colours.. i was think a dark background with charcoal letters so something along those colour schumes but im open to ideas..

Business

BRL Constructions

```html
<!DOCTYPE html>
<html lang="en">
<head>
<meta charset="utf-8">
<title>BRL Constructions – Business Card</title>
<link rel="stylesheet" href="https://fonts.googleapis.com/css2?family=Arimo:wght@400;700&display=swap">
<style>
  :root {
    --page-bg: #8d97a3;
    --card-bg: #231f20;
    --accent-red: #ed1c24;
    --text-white: #ffffff;
    --logo-silver: #c9c9c9;
  }
  html, body {
    margin: 0;
    width: 1200px;
    height: 900px;
    overflow: hidden;
    background: var(--page-bg);
    font-family: "Arimo", Arial, sans-serif;
  }
  .business-card {
    position: absolute;
    left: 100px;
    top: 165px;
    width: 1000px;
    height: 570px;
    background: var(--card-bg);
    overflow: hidden;
    box-shadow: 0 10px 30px rgba(0,0,0,0.35);
  }
  .card-graphics {
    position: absolute;
    inset: 0;
  }
  .brand-name {
    position: absolute;
    left: 560px;
    top: 92px;
    margin: 0;
    color: var(--logo-silver);
    font-weight: 700;
    font-size: 34px;
    letter-spacing: 3px;
    text-transform: uppercase;
    white-space: nowrap;
  }
  .holder-name {
    position: absolute;
    right: 470px;
    top: 366px;
    margin: 0;
    color: var(--text-white);
    font-weight: 700;
    font-size: 34px;
    white-space: nowrap;
  }
  .contact-list {
    position: absolute;
    left: 640px;
    top: 218px;
    margin: 0;
    padding: 0;
    list-style: none;
  }
  .contact-item {
    display: flex;
    align-items: center;
    height: 50px;
    color: var(--text-white);
    font-size: 25px;
  }
  .contact-icon {
    width: 30px;
    height: 30px;
    margin-right: 22px;
    flex: none;
  }
</style>
</head>
<body>
  <div class="business-card">
    <svg class="card-graphics" width="1000" height="570" viewBox="0 0 1000 570">
      <polygon class="name-band" points="0,352 560,352 571,428 0,428" fill="var(--accent-red)"/>
      <line class="divider-line" x1="545" y1="185" x2="600" y2="570" stroke="var(--accent-red)" stroke-width="4"/>
    </svg>

    <p class="brand-name">BRL Constructions</p>

    <p class="holder-name">Your Name goes here</p>

    <ul class="contact-list">
      <li class="contact-item">
        <svg class="contact-icon" viewBox="0 0 30 30" aria-hidden="true">
          <circle cx="15" cy="15" r="13" fill="none" stroke="var(--accent-red)" stroke-width="3"/>
          <path d="M10 9.5c1-1 2-1 2.6 0l1 1.8c.4.7.2 1.3-.4 1.8l-.6.5c.6 1.5 1.8 2.7 3.3 3.3l.5-.6c.5-.6 1.1-.8 1.8-.4l1.8 1c1 .6 1 1.6 0 2.6-1.2 1.2-3.2 1.2-5.6-.5-1.9-1.3-3.5-2.9-4.8-4.8-1.7-2.4-1.7-4.4-.5-5.6z" fill="var(--text-white)"/>
        </svg>
        <span class="contact-text">0498765432</span>
      </li>
      <li class="contact-item">
        <svg class="contact-icon" viewBox="0 0 30 30" aria-hidden="true">
          <circle cx="15" cy="15" r="13" fill="none" stroke="var(--accent-red)" stroke-width="3"/>
          <rect x="8.5" y="10" width="13" height="10" fill="none" stroke="var(--text-white)" stroke-width="1.6"/>
          <polyline points="8.5,10 15,15.5 21.5,10" fill="none" stroke="var(--text-white)" stroke-width="1.6"/>
        </svg>
        <span class="contact-text">yourname@brlmail.com</span>
      </li>
      <li class="contact-item">
        <svg class="contact-icon" viewBox="0 0 30 30" aria-hidden="true">
          <circle cx="15" cy="15" r="13" fill="none" stroke="var(--accent-red)" stroke-width="3"/>
          <text x="15" y="18.5" text-anchor="middle" font-family="Arimo, Arial, sans-serif" font-size="9" font-weight="700" fill="var(--text-white)">abn</text>
        </svg>
        <span class="contact-text">51824753</span>
      </li>
    </ul>
  </div>
</body>
</html>
```